Sales Tip from Ned Valcourt- Think Like a Buyer-

I am a sales trainer for B2B sales teams. I would like you to create an infographic that my learners can view, easily understand and immediately apply to their day to day work.
The graphic should:
1-Display the title on top- Sales Tip from Ned Valcourt- Think Like a Buyer
2- Please use the writing and layout from the attachment.
3- Create a tagline at the bottom that says- Top B2B Sales Teams, Sell The Way Thier Clients Buy.
Our company colors are red, silver with slight black trim.
I do not like cartoon like graphics. This must be poweful...
Updates

thank you very much for your consideration. looking forward to seeing your work Ned

Target Market(s)

CEO's of B2B Technology Companies

Font styles to use
Sans Serif

Requirements
Must have
• the apility to attach to a powerpoint slide. company colors...red, silver and a little black
Should not have
• cartoon animation, business,

```html
<!DOCTYPE html>
<html lang="en">
<head>
<meta charset="utf-8">
<title>Sales Tip from Ned Valcourt – Think Like a Buyer</title>
<link rel="stylesheet" href="https://fonts.googleapis.com/css2?family=Poppins:ital,wght@0,500;0,600;0,700;1,700&family=Questrial&display=swap">
<style>
  :root {
    --page-bg: #e6e6e6;
    --red-bright: #ff1a1a;
    --red-mid: #d40000;
    --red-deep: #6e0000;
    --black: #000000;
    --silver-light: #f4f4f4;
    --silver-mid: #c9c9c9;
    --silver-dark: #8d8d8d;
    --seller-fill-a: #f6dada;
    --seller-fill-b: #b9a9a9;
    --buyer-fill: #7a0000;
    --buyer-fill-b: #5c0000;
    --text-dark: #1a1a1a;
    --text-light: #ffffff;
  }
  * { box-sizing: border-box; margin: 0; padding: 0; }
  html, body { width: 1200px; height: 849px; overflow: hidden; }
  body { background: var(--page-bg); position: relative; font-family: "Questrial", sans-serif; }

  .sales-tip {
    position: absolute;
    left: 270px; top: 87px;
    width: 660px; height: 672px;
    overflow: hidden;
    background:
      radial-gradient(ellipse 70% 30% at 85% 8%, rgba(255,90,90,.55), transparent 70%),
      linear-gradient(160deg, var(--red-deep) 0%, var(--red-mid) 22%, var(--red-bright) 45%, var(--red-mid) 62%, #3a0000 82%, var(--black) 96%);
  }

  .silver-text {
    background: linear-gradient(180deg, var(--silver-light) 0%, var(--silver-mid) 55%, var(--silver-dark) 100%);
    -webkit-background-clip: text; background-clip: text;
    color: transparent;
  }

  .tip-byline {
    position: absolute; top: 40px; left: 0; width: 100%;
    text-align: center;
    font-family: "Poppins", sans-serif; font-weight: 600;
    font-size: 30px; letter-spacing: 1px; line-height: 1.2;
  }
  .tip-title {
    position: absolute; top: 80px; left: 0; width: 100%;
    text-align: center;
    font-family: "Poppins", sans-serif; font-weight: 700;
    font-size: 43px; letter-spacing: 1px; line-height: 1.2;
  }

  .column-label {
    position: absolute; top: 150px; width: 279px;
    text-align: center;
    font-family: "Poppins", sans-serif; font-weight: 600;
    font-size: 26px; line-height: 1.3;
  }
  .column-label--seller { left: 33px; }
  .column-label--buyer { left: 348px; color: var(--black); }

  .question-card {
    position: absolute; top: 187px; width: 279px; height: 396px;
    border-radius: 16px;
    padding: 30px 12px 0;
    display: flex; flex-direction: column; align-items: center; gap: 26px;
    text-align: center; list-style: none;
    font-size: 16.5px; line-height: 1.42;
  }
  .question-card--seller {
    left: 33px;
    border: 4px solid var(--silver-mid);
    box-shadow: 0 0 0 3px var(--red-bright);
    background: linear-gradient(135deg, var(--seller-fill-a) 0%, #e2caca 45%, var(--seller-fill-b) 100%);
    color: var(--text-dark);
  }
  .question-card--buyer {
    left: 348px;
    border: 4px solid var(--red-mid);
    box-shadow: 0 0 0 3px #2a0000;
    background: linear-gradient(180deg, var(--buyer-fill) 0%, var(--buyer-fill-b) 100%);
    color: var(--text-light);
    gap: 24px;
  }

  .tagline {
    position: absolute; top: 608px; left: 0; width: 100%;
    text-align: center;
    font-family: "Poppins", sans-serif; font-weight: 700; font-style: italic;
    font-size: 19px; letter-spacing: 0.5px;
    color: var(--text-light);
  }
</style>
</head>
<body>
  <main class="sales-tip">
    <p class="tip-byline silver-text">SALES TIP FROM NED VALCOURT</p>
    <h1 class="tip-title silver-text">THINK LIKE A BUYER</h1>

    <h2 class="column-label column-label--seller silver-text">SELLER</h2>
    <h2 class="column-label column-label--buyer">BUYER</h2>

    <ol class="question-card question-card--seller">
      <li>1. DO THEY LIKE US?</li>
      <li>2. DO THEY LIKE<br>OUR PRODUCT BETTER<br>THAN COMPETITION?</li>
      <li>3. WILL THEY ACCEPT<br>OUR PRICE?</li>
      <li>4. CAN WE CLOSE IT<br>QUICKLY WITHOUT<br>BEING TOO PUSHY?</li>
    </ol>

    <ol class="question-card question-card--buyer">
      <li>1. HOW WILL THIS IMPACT<br>OUR BUSINESS?</li>
      <li>2. WHAT RISKS OR<br>DISRUPTIONS<br>COULD OCCUR?</li>
      <li>3. WHY DO WE NEED<br>TO DO THIS NOW?</li>
      <li>4. WHY THEM AND<br>NOT COMPETITION?</li>
      <li>5. WHAT ARE ALL COSTS?<br>IS IT A FAIR DEAL?</li>
    </ol>

    <p class="tagline">TOP B2B SALES TEAMS, SELL THE WAY THEIR CLIENTS BUY</p>
  </main>
</body>
</html>
```